Design A Container For Dog Leash

I need packaging designed based off of this template below.

For Front:
Make header the Steady Paw colors and logo

Header:
Steady Paw Adjustable Dog Leash (logo in top right corner)

Bullet Points Below Main Header;
-3'-5’ Adjustable Leash
-Heel Tightening Training Leash
-Hands Free Leash
-Slip Leash

Back TOP of package:
1, (logo in top right corner)
2, Steady Paw Adjustable Dog Leash

Text on Bottom Back of Package:
Steady Paw Adjustable Dog Leash
-3'-5’ Adjustable Leash
-Hands Free Leash
-Slip Leash

Made in China

Available At:
www.TrailHoundGear.com

I have attached the package specifications and the logo to be used.

Also, the website is:
www.TrailHoundGear.com so you can see the color scheme (the logo).

```html
<!DOCTYPE html>
<html lang="en">
<head>
<meta charset="utf-8">
<title>Steady Paw Adjustable Dog Leash – Packaging</title>
<link rel="stylesheet" href="https://fonts.googleapis.com/css2?family=Archivo+Black&family=Roboto:wght@700&display=swap">
<style>
  :root{
    --canvas:#ffffff;
    --ink:#111111;
    --white:#ffffff;
    --brand-red:#e0001b;
    --deep-red:#6e0010;
    --wine:#3a0006;
    --slate:#2c2c2e;
    --steel:#9a9a9a;
    --royal-blue:#1432b8;
    --frame-blue:#3a4aa8;
  }
  *{box-sizing:border-box;margin:0;padding:0}
  html,body{width:1200px;height:675px;overflow:hidden;background:var(--canvas)}
  .canvas{position:relative;width:1200px;height:675px}

  .card{position:absolute;top:40px;height:600px}
  .hole{position:absolute;width:17px;height:17px;border-radius:50%}
  .hang-slot{position:absolute;border-radius:8px}
  .brand-mark{position:absolute;display:flex;align-items:center;gap:3px;
    font-family:"Roboto",sans-serif;font-weight:700;font-size:8px;line-height:1;text-transform:uppercase}
  .brand-mark .mark-square{width:7px;height:7px;flex:none}

  /* Front */
  .front{left:369px;width:227px;
    background:linear-gradient(180deg,#1c1c1e 0%,#8d8d8f 24%,#6a0a14 38%,var(--deep-red) 58%,#5a000c 72%,var(--wine) 84%,#8e0014 100%)}
  .front .hero-photo{position:absolute;left:0;top:0;width:100%;height:168px;
    background:linear-gradient(180deg,#2a2a2c 0%,#5b5048 45%,#b08a5a 70%,rgba(140,140,140,0) 100%)}
  .front .inner-frame{position:absolute;left:8px;top:8px;right:8px;bottom:8px;
    border:1px solid var(--frame-blue);border-radius:10px}
  .front .hang-slot{left:84px;top:20px;width:34px;height:9px;border:1px solid var(--frame-blue)}
  .front .brand-mark{left:150px;top:18px;color:var(--white)}
  .front .brand-mark .mark-square{background:var(--brand-red)}
  .front .title-block{position:absolute;left:0;top:148px;width:100%;text-align:center;transform:rotate(-7deg)}
  .front .product-name{font-family:"Archivo Black",sans-serif;font-size:33px;line-height:1;color:var(--white);
    -webkit-text-stroke:6px var(--ink);paint-order:stroke fill}
  .front .product-variant{font-family:"Archivo Black",sans-serif;font-size:21px;line-height:1.1;color:var(--white);
    -webkit-text-stroke:5px var(--ink);paint-order:stroke fill;margin-left:30px}
  .front .feature-panel{position:absolute;left:0;top:256px;width:124px;height:35px;
    background:var(--royal-blue);border:1px solid #dfe4ff;border-left:none;border-radius:0 6px 6px 0;
    padding:4px 6px;list-style:none}
  .front .feature-panel li{font-family:"Roboto",sans-serif;font-weight:700;font-size:5.5px;line-height:1.25;
    color:var(--white);text-transform:uppercase}
  .front .hole{border:1px solid #d9c7c9}

  /* Back */
  .back{left:651px;width:230px;background:var(--white);border:1px solid var(--brand-red)}
  .back .inner-frame{position:absolute;left:12px;top:8px;right:12px;bottom:10px;
    border:1.5px solid var(--brand-red);border-radius:12px}
  .back .hang-slot{left:80px;top:23px;width:46px;height:14px;border:1.5px solid var(--brand-red)}
  .back .brand-mark{left:146px;top:48px;color:var(--brand-red)}
  .back .brand-mark .mark-square{background:var(--ink)}
  .back .title-block{position:absolute;left:0;top:107px;width:100%;text-align:center}
  .back .product-name{font-family:"Archivo Black",sans-serif;font-size:31px;line-height:1;color:var(--ink);
    -webkit-text-stroke:8px var(--ink);paint-order:stroke fill;position:relative}
  .back .product-name span,.back .product-variant span{position:relative}
  .back .product-name span{-webkit-text-stroke:4px var(--white);color:var(--ink)}
  .back .product-variant{font-family:"Archivo Black",sans-serif;font-size:20px;line-height:1.2;margin-top:10px;color:var(--white);
    -webkit-text-stroke:6px var(--ink);paint-order:stroke fill}
  .back .hole{border:1.5px solid var(--ink)}
  .back .info-panel{position:absolute;left:30px;top:321px;width:166px;height:111px;background:var(--brand-red);
    border-radius:6px;padding:9px 6px;text-align:center;color:var(--white);
    font-family:"Roboto",sans-serif;font-weight:700;font-size:5.5px;line-height:1.3;text-transform:uppercase}
  .back .info-panel ul{list-style:none}
  .back .info-panel .origin{margin-top:8px}
  .back .info-panel .stockist{margin-top:8px}
</style>
</head>
<body>
<main class="canvas">

  <section class="card front" aria-label="Package front">
    <div class="hero-photo" role="img" aria-label="Photo of two happy dogs, a dark shaggy dog and a golden retriever"></div>
    <div class="inner-frame"></div>
    <div class="hang-slot"></div>
    <div class="brand-mark"><span class="mark-square"></span>Steady Paw</div>
    <div class="title-block">
      <h1 class="product-name">DOG LEASH</h1>
      <p class="product-variant">K9 Adjustable</p>
    </div>
    <ul class="feature-panel">
      <li>3'-5' Adjustable Leash</li>
      <li>Heel Tightening Training Leash</li>
      <li>Hands Free Leash</li>
      <li>Slip Leash</li>
    </ul>
    <span class="hole" style="left:66px;top:299px"></span>
    <span class="hole" style="left:148px;top:299px"></span>
    <span class="hole" style="left:63px;top:476px"></span>
    <span class="hole" style="left:146px;top:476px"></span>
  </section>

  <section class="card back" aria-label="Package back">
    <div class="inner-frame"></div>
    <div class="hang-slot"></div>
    <div class="brand-mark"><span class="mark-square"></span>Steady Paw</div>
    <div class="title-block">
      <h2 class="product-name"><span>DOG LEASH</span></h2>
      <p class="product-variant">K9 Adjustable</p>
    </div>
    <span class="hole" style="left:65px;top:281px"></span>
    <span class="hole" style="left:148px;top:281px"></span>
    <span class="hole" style="left:62px;top:459px"></span>
    <span class="hole" style="left:145px;top:459px"></span>
    <div class="info-panel">
      <ul>
        <li>Steady Paw Adjustable Dog Leash</li>
        <li>3'-5' Adjustable Leash</li>
        <li>Heel Tightening Training Leash</li>
        <li>Hands Free Leash</li>
        <li>Slip Leash</li>
      </ul>
      <p class="origin">Made in China</p>
      <p class="stockist">Available at:<br>www.TrailHoundGear.com</p>
    </div>
  </section>

</main>
</body>
</html>
```